Ferncrest Dental, LLC business card project

Business card to be designed with current logo.
Dental office- please keep design of card that looks clean and professional.
Please include the following info:
Ferncrest Dental, LLC
Dr. Lorna Pettigrew
2871 Marlowe Street
Bethlehem, PA 18093
610-555-0193
ferncrestdental.office@examplemail.test
Hello everyone-
Reason: Just got back from overseas- will look at all designs and provide feedback. Thank you!
Reason: Polling my friends for the final selection-
thank you to all those that participated- so many talented designers!

```html
<!DOCTYPE html>
<html lang="en">
<head>
<meta charset="utf-8">
<title>Ferncrest Dental, LLC – Business Card</title>
<link rel="stylesheet" href="https://fonts.googleapis.com/css2?family=Open+Sans:wght@700&display=swap">
<style>
  :root {
    --green-glow: #d9ffc9;
    --green-field: #5ee84a;
    --green-deep: #3fdc2a;
    --bar-bright: #3ff020;
    --bar-mid: #6eef4e;
    --bar-pale: #b8f7a2;
    --band-bright: #2fdc10;
    --band-mid: #63ef3a;
    --band-pale: #c9ffaf;
    --shade: #8fb07e;
    --panel: #ffffff;
    --brand: #66cc11;
    --ink: #111111;
    --name: #ffffff;
  }
  html, body {
    margin: 0;
    padding: 0;
    width: 1200px;
    height: 695px;
    overflow: hidden;
    background: #ffffff;
  }
  .card {
    display: block;
    width: 1200px;
    height: 695px;
  }
  .card text {
    font-family: "Open Sans", "DejaVu Sans", Verdana, sans-serif;
    font-weight: 700;
  }
  .brand-name { fill: var(--brand); font-size: 50px; }
  .brand-dot { fill: var(--brand); }
  .doctor-name { fill: var(--name); font-size: 46px; letter-spacing: 1px; }
  .company { fill: var(--ink); font-size: 26px; }
  .contact { fill: var(--ink); font-size: 24px; }
  .address { fill: var(--ink); font-size: 21px; }
</style>
</head>
<body>
<svg class="card" viewBox="0 0 1122 650" preserveAspectRatio="none" xmlns="http://www.w3.org/2000/svg">
  <defs>
    <radialGradient id="field" cx="0.72" cy="0.35" r="0.9">
      <stop offset="0" stop-color="var(--green-field)"/>
      <stop offset="0.55" stop-color="#74ea5e"/>
      <stop offset="1" stop-color="#c9f7bb"/>
    </radialGradient>
    <radialGradient id="glow" cx="0" cy="0.75" r="0.42">
      <stop offset="0" stop-color="#ffffff"/>
      <stop offset="0.6" stop-color="var(--green-glow)" stop-opacity="0.7"/>
      <stop offset="1" stop-color="var(--green-glow)" stop-opacity="0"/>
    </radialGradient>
    <filter id="name-shadow" x="-5%" y="-30%" width="110%" height="160%">
      <feDropShadow dx="2" dy="3" stdDeviation="1.5" flood-color="#000" flood-opacity="0.75"/>
    </filter>
    <filter id="soft-shadow" x="-5%" y="-30%" width="110%" height="160%">
      <feDropShadow dx="1" dy="2" stdDeviation="1" flood-color="#ffffff" flood-opacity="0.6"/>
    </filter>
  </defs>

  <!-- Background -->
  <rect class="background" width="1122" height="650" fill="url(#field)"/>
  <rect class="background-glow" width="1122" height="650" fill="url(#glow)"/>

  <!-- Vertical bars -->
  <g class="frame-bars">
    <rect x="94" y="0" width="64" height="378" fill="var(--bar-bright)"/>
    <rect x="158" y="0" width="62" height="443" fill="var(--bar-mid)"/>
    <rect x="220" y="0" width="63" height="508" fill="var(--bar-pale)"/>
    <rect x="158" y="432" width="62" height="11" fill="var(--shade)" opacity="0.6"/>
    <rect x="220" y="498" width="63" height="10" fill="var(--shade)" opacity="0.6"/>
  </g>

  <!-- Horizontal bands with mitred corners -->
  <g class="frame-bands">
    <polygon points="94,378 1122,378 1122,432 155,432" fill="var(--band-bright)"/>
    <polygon points="158,443 1122,443 1122,498 215,498" fill="var(--band-mid)"/>
    <polygon points="220,508 1122,508 1122,562 275,562" fill="var(--band-pale)"/>
  </g>

  <!-- Brand panel -->
  <g class="brand-panel">
    <rect x="284" y="64" width="766" height="134" fill="var(--panel)"/>
    <circle class="brand-dot" cx="440" cy="131" r="18"/>
    <text class="brand-name" x="474" y="149">Ferncrest Dental</text>
  </g>

  <!-- Identity -->
  <text class="doctor-name" x="297" y="250" filter="url(#name-shadow)">Dr. Lorna Pettigrew</text>
  <text class="company" x="533" y="305" filter="url(#soft-shadow)">Ferncrest Dental, LLC</text>

  <!-- Contact details -->
  <text class="contact" x="620" y="416" filter="url(#soft-shadow)">610-555-0193</text>
  <text class="contact" x="614" y="479" filter="url(#soft-shadow)">ferncrestdental.office@examplemail.test</text>
  <text class="address" x="620" y="528" filter="url(#soft-shadow)">2871 Marlowe Street</text>
  <text class="address" x="620" y="558" filter="url(#soft-shadow)">Bethlehem, PA 18093</text>
</svg>
</body>
</html>
```